Startup Drone Platform Company business card

We are needing a business card design for our employees. We are a startup drone platform. We are looking for a business card that has our logo on one side, with the employee/company details on the opposite side. We are looking for something that is very eye catching, modern, and bold.

Target Market(s)

This will target both drone pilots and drone businesses, along with all the industries that could utilize drone services (aerial video, aerial photos, inspections, 3d mapping, etc).

Industry/Entity Type

Business

```html
<!DOCTYPE html>
<html lang="en">
<head>
<meta charset="utf-8">
<title>Aero Task – Business Card</title>
<link rel="stylesheet" href="https://fonts.googleapis.com/css2?family=Lato:wght@400;700;900&family=Montserrat:wght@400;500&display=swap">
<style>
  :root {
    --bg: #e9e6e1;
    --card: #030303;
    --teal: #3fb8c4;
    --teal-deep: #1f6f77;
    --white: #ffffff;
    --grey: #9a9a9a;
    --card-w: 550px;
    --card-h: 314px;
  }
  * { margin: 0; padding: 0; box-sizing: border-box; }
  html, body {
    width: 1200px; height: 789px; overflow: hidden;
    background: var(--bg);
  }
  .sheet {
    position: relative; width: 1200px; height: 789px;
    display: flex; align-items: center; justify-content: center; gap: 40px;
  }
  .card {
    position: relative; width: var(--card-w); height: var(--card-h);
    background: var(--card); overflow: hidden;
    box-shadow: 0 10px 26px rgba(0,0,0,.25);
  }
  .band {
    position: absolute; left: 0; right: 0;
    background: linear-gradient(90deg, rgba(63,184,196,0) 0%, rgba(31,111,119,.55) 45%, var(--teal) 100%);
  }

  /* Front */
  .card--front .band { top: 214px; height: 44px; }
  .brand-mark {
    position: absolute; left: 0; right: 0; top: 62px;
    display: flex; flex-direction: column; align-items: center; gap: 18px;
  }
  .brand-dot {
    width: 62px; height: 62px; border-radius: 50%;
    border: 4px solid var(--teal);
  }
  .brand-name {
    font-family: "Montserrat", sans-serif; font-weight: 500;
    font-size: 26px; letter-spacing: 10px; color: var(--white);
    padding-left: 10px;
  }

  /* Back */
  .card--back .band { top: 242px; height: 48px; }
  .holder {
    position: absolute; left: 100px; top: 128px; text-align: center;
  }
  .holder__name {
    font-family: "Lato", sans-serif; font-weight: 900;
    font-size: 31px; color: var(--teal); letter-spacing: -.5px; line-height: 1;
  }
  .holder__role {
    font-family: "Lato", sans-serif; font-weight: 400;
    font-size: 15px; color: var(--grey); letter-spacing: .5px; margin-top: 3px;
  }
  .divider {
    position: absolute; left: 318px; top: 52px; width: 2px; height: 150px;
    background: var(--teal);
  }
  .contact {
    position: absolute; left: 336px; right: 22px; top: 50px;
    font-family: "Lato", sans-serif;
  }
  .contact__address {
    color: var(--teal); font-size: 13px; line-height: 1.35; font-weight: 400;
    margin-bottom: 18px;
  }
  .contact__list { list-style: none; }
  .contact__item {
    display: flex; align-items: center; gap: 8px;
    color: var(--white); font-size: 13px; line-height: 20px;
  }
  .contact__item svg { width: 14px; height: 14px; flex: none; }
  .band__name {
    position: absolute; left: 0; right: 0; top: 0; height: 48px;
    display: flex; align-items: center; justify-content: center;
    font-family: "Montserrat", sans-serif; font-weight: 500;
    font-size: 22px; letter-spacing: 9px; color: var(--white);
  }
</style>
</head>
<body>
<main class="sheet">

  <section class="card card--front" aria-label="Card front">
    <div class="brand-mark">
      <span class="brand-dot" aria-hidden="true"></span>
      <span class="brand-name">AERO TASK</span>
    </div>
    <div class="band"></div>
  </section>

  <section class="card card--back" aria-label="Card back">
    <div class="holder">
      <p class="holder__name">YOUR NAME</p>
      <p class="holder__role">POSITION</p>
    </div>
    <div class="divider"></div>
    <div class="contact">
      <p class="contact__address">PO BOX 1234, Address Line 1,<br>Address Line 2,</p>
      <ul class="contact__list">
        <li class="contact__item">
          <svg viewBox="0 0 16 16" fill="#fff" aria-hidden="true"><path d="M2 6c0-2 2-3 6-3s6 1 6 3v1h-3V6H5v1H2z"/><rect x="3" y="8" width="10" height="6" rx="1"/></svg>
          123-456-7890
        </li>
        <li class="contact__item">
          <svg viewBox="0 0 16 16" fill="#fff" aria-hidden="true"><rect x="4" y="1" width="8" height="4"/><rect x="1" y="6" width="14" height="6" rx="1"/><rect x="4" y="10" width="8" height="5" fill="#fff" stroke="#000" stroke-width="1"/></svg>
          123-456-7890
        </li>
        <li class="contact__item">
          <svg viewBox="0 0 16 16" aria-hidden="true"><rect x="1" y="3" width="14" height="10" fill="#fff"/><path d="M1 3l7 6 7-6" fill="none" stroke="#000" stroke-width="1.2"/></svg>
          youremail@example.com
        </li>
        <li class="contact__item">
          <svg viewBox="0 0 16 16" fill="none" stroke="#fff" stroke-width="1.2" aria-hidden="true"><circle cx="8" cy="8" r="6.5"/><ellipse cx="8" cy="8" rx="3" ry="6.5"/><path d="M1.5 8h13M2.5 5h11M2.5 11h11"/></svg>
          www.website.com
        </li>
      </ul>
    </div>
    <div class="band">
      <span class="band__name">AERO TASK</span>
    </div>
  </section>

</main>
</body>
</html>
```